Artificial intelligence, machine learning, and automation company needs a sexy business card design

We need a sleek and sexy business card design for an AI consulting company based in Philadelphia PA. We provide custom machine learning and automation solutions for companies of all shapes and sizes. The primary industries that we serve are pharmaceuticals, engineering, healthcare, and computer software. We would like the designs to be a black business card that uses green as a sleek accent color. The final design should communicate intelligence, cutting edge new-tech, and optimization.

Target Market(s)

C-level and VP level executives of multi-million annual companies. Mostly in Pharma, Healthcare, Real Estate, Retail, and Engineering

Industry/Entity Type

Computer Software

Contact Information for Business Card

Name: Jed Harlow
Title: CEO
Cell: 484 562 0937
Email: JedH@quillorbit.example
Website: www.QuillOrbit.example

Font styles to use
Sans Serif

Colors

Designer to choose colors to be used in the design.

Requirements
Must have
• 1) Attached Quillon Logo (either with colors or not/embossed)
• 2) "Artificial Intelligence" "Automation" and "Machine Learning"
• 3) "Quillon Laboratories" or "Quillon Labs" or "Quillon"
• 4) Sexy AF.
Nice to have
• Black card / dark card color, "Quillon Green" accent colors (in attached .ai file), Embossment of logo/name/etc, thick card stock, colored borders (on card sides, not front/back faces)
Should not have
• Should not be bland, or unsexy.

```html
<!DOCTYPE html>
<html lang="en">
<head>
<meta charset="utf-8">
<title>Quillon Laboratories – Business Card</title>
<link href="https://fonts.googleapis.com/css2?family=Montserrat:wght@400;500;700&display=swap" rel="stylesheet">
<style>
  :root {
    --backdrop: #1b1b1d;
    --card: #121126;
    --card-edge: #0d0c1d;
    --gold: #c9a54c;
    --gold-soft: #b8984a;
    --ink-dark: #1a1708;
  }
  * { margin: 0; padding: 0; box-sizing: border-box; }
  html, body {
    width: 1200px; height: 900px; overflow: hidden;
    background: var(--backdrop);
    font-family: "Montserrat", Arial, sans-serif;
  }
  .stage { position: relative; width: 1200px; height: 900px; }
  .card {
    position: absolute; top: 130px; width: 370px; height: 640px; overflow: hidden;
    background: linear-gradient(180deg, var(--card) 0%, var(--card-edge) 100%);
    color: var(--gold);
    text-align: center;
  }
  .card--front { left: 217px; }
  .card--back { left: 600px; }
  .line { position: absolute; left: 0; right: 0; }
  .holder-name { top: 66px; font-size: 23px; line-height: 28px; font-weight: 700; letter-spacing: 1px; }
  .holder-title { top: 100px; font-size: 13px; line-height: 18px; font-weight: 400; letter-spacing: 1.2px; color: var(--gold-soft); }
  .rule {
    position: absolute; left: 50%; width: 18px; height: 2px;
    margin-left: -9px; background: var(--gold);
  }
  .brand-mark {
    position: absolute; left: 50%; top: 219px; width: 60px; height: 60px;
    margin-left: -30px; border: 4px solid var(--gold);
  }
  .brand-name {
    top: 322px; font-size: 31px; font-weight: 400; letter-spacing: 6px; line-height: 38px;
    padding-left: 6px;
  }
  .brand-name span { display: block; font-size: 15px; letter-spacing: 4px; line-height: 20px; }
  .address { top: 398px; font-size: 15px; line-height: 25px; font-weight: 500; }
  .contact-icons {
    position: absolute; top: 467px; left: 0; right: 0;
    display: flex; justify-content: center; gap: 16px;
  }
  .contact-icon {
    width: 22px; height: 22px; border-radius: 50%; background: var(--gold);
    display: flex; align-items: center; justify-content: center;
  }
  .contact-list { top: 505px; font-size: 15px; line-height: 24px; font-weight: 500; }
  .services { top: 437px; font-size: 15px; font-weight: 500; letter-spacing: 0.6px; line-height: 34px; }
</style>
</head>
<body>
<main class="stage">
  <section class="card card--front" aria-label="Card front">
    <h1 class="line holder-name">JED HARLOW</h1>
    <p class="line holder-title">CHIEF EXECUTIVE OFFICER</p>
    <div class="rule" style="top:127px"></div>
    <span class="brand-mark" aria-hidden="true"></span>
    <p class="line brand-name">QUILLON<span>LABORATORIES</span></p>
    <p class="line address">2750 Fernhill Ave<br>Philadelphia PA, 19130</p>
    <div class="contact-icons">
      <span class="contact-icon" aria-label="Phone">
        <svg width="12" height="12" viewBox="0 0 24 24"><path fill="var(--ink-dark)" d="M6.6 10.8a15 15 0 0 0 6.6 6.6l2.2-2.2c.3-.3.7-.4 1-.2 1.1.4 2.300.6 3.6.6.6 0 1 .4 1 1V20c0 .6-.4 1-1 1A17 17 0 0 1 3 4c0-.6.4-1 1-1h3.5c.6 0 1 .4 1 1 0 1.3.2 2.5.6 3.6.1.3 0 .7-.2 1z"/></svg>
      </span>
      <span class="contact-icon" aria-label="Email">
        <svg width="12" height="12" viewBox="0 0 24 24"><rect x="2" y="5" width="20" height="14" rx="2" fill="var(--ink-dark)"/><path d="M3 6l9 7 9-7" stroke="var(--gold)" stroke-width="2" fill="none"/></svg>
      </span>
      <span class="contact-icon" aria-label="Website">
        <svg width="12" height="12" viewBox="0 0 24 24" fill="none" stroke="var(--ink-dark)" stroke-width="2.6" stroke-linecap="round"><path d="M10 14a4 4 0 0 0 5.7 0l3-3a4 4 0 0 0-5.7-5.7l-1 1"/><path d="M14 10a4 4 0 0 0-5.7 0l-3 3a4 4 0 0 0 5.7 5.7l1-1"/></svg>
      </span>
    </div>
    <p class="line contact-list">484 562 0937<br>JedH@quillorbit.example<br>quillorbit.example</p>
  </section>

  <section class="card card--back" aria-label="Card back">
    <span class="brand-mark" aria-hidden="true"></span>
    <p class="line brand-name">QUILLON<span>LABORATORIES</span></p>
    <div class="rule" style="top:426px"></div>
    <p class="line services">Artificial Intelligence<br>Machine Learning<br>Automation</p>
    <div class="rule" style="top:555px"></div>
  </section>
</main>
</body>
</html>
```